Bright Ridge Painting and Remodeling New Facebook Design Project

Facebook should include company logo.

Name of company: Bright Ridge Painting and Remodeling
Address: 4612 NW 28th st Suite 519
Miami, FL 33174

local phone: (305) 555-0147
toll free (855) 555-0192
fax (866) 555-0136

email: corla@paintingbrightridge.example

let me know if links to other social media should be included.

company does interior and exterior painting, staining, pressure washing, wall paper removal, tile installation, tile removal, specializing in vinyl floor removal and any of your remodeling needs.

we give free estimates.

Designer can add nice pictures of homes showing painting of interior exterior etc.

Or even videos or whatever they feel is necessary to make an impression to consumers.

Be creative. Page should be professional but eye catching.

Reason: I started getting good designs submitted on the last day want to give designers an opportunity to submit more

Industry/Entity Type

Painting And Decorating

Requirements
Must have
• Professional wording/ font and pictures.
• Creative professional design and colors.
Nice to have
• Pictures of the services offered
• Videos about/and or of the services being offered
Should not have
• N/A

```html
<!DOCTYPE html>
<html lang="en">
<head>
<meta charset="utf-8">
<title>Bright Ridge Painting and Remodeling – Cover</title>
<link href="https://fonts.googleapis.com/css2?family=Montserrat:wght@500;600;700;800&display=swap" rel="stylesheet">
<style>
  :root{
    --ink:#ffffff;
    --pink:#ec1b6b;
    --pink-soft:rgba(236,27,107,.55);
    --shade:rgba(18,16,20,.6);
    --bar:rgba(92,140,190,.78);
    --room-dark-a:#3b3430;
    --room-dark-b:#14110f;
    --room-warm-a:#c9a57a;
    --room-warm-b:#6f5a45;
    --kitchen-a:#d9d6d2;
    --kitchen-b:#4a4240;
    --room-pink-a:#f0a3c4;
    --room-pink-b:#c2356f;
  }
  html,body{margin:0;padding:0;overflow:hidden;background:#fff}
  .cover{position:relative;width:1200px;height:444px;overflow:hidden;font-family:"Montserrat",sans-serif;color:var(--ink)}
  .backdrop{position:absolute;inset:0}
  .brand{position:absolute;left:160px;top:30px;display:flex;align-items:center;gap:10px}
  .brand-dot{width:34px;height:34px;border-radius:50%;background:var(--pink)}
  .brand-name{font-weight:700;font-size:17px;letter-spacing:1px}
  .title{position:absolute;left:86px;top:160px;margin:0}
  .title-main{display:block;font-weight:800;font-size:40px;letter-spacing:1px;line-height:1}
  .title-sub{display:block;font-weight:500;font-size:21px;letter-spacing:4.5px;line-height:1.25;margin-top:8px}
  .contact-btn{position:absolute;left:22px;top:290px;width:250px;height:48px;background:var(--pink);transform:skewX(-18deg);display:flex;align-items:center;justify-content:center}
  .contact-btn span{transform:skewX(18deg);font-weight:800;font-size:26px;letter-spacing:.5px}
  .call{position:absolute;right:28px;top:276px;text-align:right}
  .call-title{font-weight:800;font-size:28px;letter-spacing:1px;margin:0 0 14px}
  .call-line{font-size:15px;font-weight:500;margin:0;line-height:1.35;letter-spacing:.5px}
  .info-bar{position:absolute;left:0;right:0;bottom:0;height:73px;display:flex;align-items:center}
  .info{position:absolute;display:flex;align-items:center;gap:16px}
  .info svg{flex:none}
  .info-email{left:36px;font-size:17px;font-weight:600;letter-spacing:1px}
  .info-address{left:522px;font-size:20px;font-weight:700;line-height:1.1}
  .info-phone{left:940px;font-size:23px;font-weight:600;letter-spacing:.5px}
</style>
</head>
<body>
<div class="cover">
  <svg class="backdrop" width="1200" height="444" viewBox="0 0 1200 444">
    <defs>
      <linearGradient id="roomDark" x1="0" y1="0" x2="1" y2="1"><stop offset="0" stop-color="var(--room-dark-a)"/><stop offset="1" stop-color="var(--room-dark-b)"/></linearGradient>
      <linearGradient id="roomWarm" x1="0" y1="0" x2="0" y2="1"><stop offset="0" stop-color="var(--room-warm-a)"/><stop offset="1" stop-color="var(--room-warm-b)"/></linearGradient>
      <linearGradient id="kitchen" x1="0" y1="0" x2="0" y2="1"><stop offset="0" stop-color="var(--kitchen-a)"/><stop offset="1" stop-color="var(--kitchen-b)"/></linearGradient>
      <linearGradient id="roomPink" x1="0" y1="0" x2="1" y2="1"><stop offset="0" stop-color="var(--room-pink-a)"/><stop offset="1" stop-color="var(--room-pink-b)"/></linearGradient>
    </defs>
    <rect x="0" y="0" width="490" height="444" fill="url(#roomDark)" role="img" aria-label="Photo of a softly lit painted bedroom interior"/>
    <rect x="487" y="0" width="242" height="444" fill="url(#roomWarm)" role="img" aria-label="Photo of a modern home living room opening onto a patio"/>
    <rect x="727" y="0" width="243" height="444" fill="url(#kitchen)" role="img" aria-label="Photo of a remodeled kitchen with dark cabinets and pink pendant lights"/>
    <rect x="968" y="0" width="232" height="444" fill="url(#roomPink)" role="img" aria-label="Photo of a bright interior room"/>
    <line x1="487" y1="0" x2="487" y2="444" stroke="#fff" stroke-width="4"/>
    <line x1="727" y1="0" x2="727" y2="444" stroke="#fff" stroke-width="4"/>
    <line x1="968" y1="0" x2="968" y2="444" stroke="#fff" stroke-width="4"/>
    <polygon points="0,0 545,0 300,444 0,444" fill="var(--shade)"/>
    <polygon points="545,0 600,0 480,220" fill="rgba(18,16,20,.35)"/>
    <polygon points="1040,0 1200,0 1200,444 880,444" fill="var(--pink-soft)"/>
    <polygon points="1120,0 1200,0 1200,200" fill="rgba(255,255,255,.18)"/>
    <rect x="0" y="371" width="1200" height="73" fill="var(--bar)"/>
  </svg>

  <div class="brand"><span class="brand-dot"></span><span class="brand-name">BRIGHT RIDGE</span></div>

  <h1 class="title">
    <span class="title-main">BRIGHT RIDGE</span>
    <span class="title-sub">PAINTING AND<br>REMODELING</span>
  </h1>

  <div class="contact-btn"><span>CONTACT US</span></div>

  <div class="call">
    <p class="call-title">CALL US</p>
    <p class="call-line">Toll free&nbsp; (855) 555-0192</p>
    <p class="call-line">Fax&nbsp; (866) 555-0136</p>
  </div>

  <div class="info-bar">
    <div class="info info-email">
      <svg width="32" height="24" viewBox="0 0 32 24"><rect x="1.5" y="1.5" width="29" height="21" fill="none" stroke="#fff" stroke-width="2.5"/><polyline points="2,3 16,14 30,3" fill="none" stroke="#fff" stroke-width="2.5"/></svg>
      <span>corla@paintingbrightridge.example</span>
    </div>
    <div class="info info-address">
      <svg width="34" height="30" viewBox="0 0 34 30"><polyline points="2,15 17,2 32,15" fill="none" stroke="#fff" stroke-width="2.5"/><polyline points="7,11 7,28 27,28 27,11" fill="none" stroke="#fff" stroke-width="2.5"/><rect x="14" y="18" width="6" height="10" fill="none" stroke="#fff" stroke-width="2.5"/></svg>
      <span>4612 NW 28th st Suite 519<br>Miami, FL 33174</span>
    </div>
    <div class="info info-phone">
      <svg width="28" height="30" viewBox="0 0 24 24"><path fill="#fff" d="M6.6 10.8a15.1 15.1 0 0 0 6.6 6.6l2.2-2.2a1 1 0 0 1 1-.25 11.4 11.4 0 0 0 3.6.57 1 1 0 0 1 1 1V20a1 1 0 0 1-1 1A17 17 0 0 1 3 4a1 1 0 0 1 1-1h3.5a1 1 0 0 1 1 1c0 1.25.2 2.45.57 3.57a1 1 0 0 1-.25 1z"/></svg>
      <span>305 555-0147</span>
    </div>
  </div>
</div>
</body>
</html>
```